Kavak Verbatica web design: a translation company with corporate clients

Need a new website for my translation and localization company with file uploading capacity directed to email for quotation

old (very old) web site is www.kvkyazim.com you can use the content text there or lorem ipsum, We will provide the texts. It will be in English - Turkish - French and German
For the content and overall layout: https://www.plumbelinguals.com/

For the color scheme you'll need to see logo's colors.

I am rebranding so new logo is uploaded The new adress will be www.kavakverbatica.com
Updates

Target Market(s)

Primarily corporate clients

Industry/Entity Type

It Company

Coding

Coded - Design and coding required

Number of Pages Required

5+ page

Font styles to use
Other font styles liked:
• Calibri

Requirements
Must have
• References on homepage (logos will be sent during design phase)
• Services: Translation, Interpretation, Localization&Consultancy, Translation API
• Quotation Form and file uploading
• Simple layout evoking reliability, speed and accuracy
Nice to have
• For the content and overall layout: https://www.plumbelinguals.com/
• Separate page for Translation Services: Marketing Translation, Legal Translation, Technical Translation, Personal Translation
• and texts under these headings
Should not have
• Old style
• Complex design

```html
<!DOCTYPE html>
<html lang="en">
<head>
<meta charset="utf-8">
<title>Kavak Verbatica — Translation, Localization &amp; Consultancy</title>
<link href="https://fonts.googleapis.com/css2?family=Lato:wght@400;700;900&family=Raleway:wght@300;400;600;700&display=swap" rel="stylesheet">
<style>
:root{
  --green:#335f0c;
  --green-dark:#274a08;
  --orange:#f7941d;
  --ink:#222;
  --body:#444;
  --muted:#888;
  --line:#d0d0d0;
  --dark:#1e1e1e;
  --footer:#161616;
  --white:#fff;
}
*{margin:0;padding:0;box-sizing:border-box}
html,body{width:1200px;height:2927px;overflow:hidden}
body{position:relative;background:var(--white);font-family:'Lato',sans-serif;color:var(--body)}
.abs{position:absolute}
.topbar{left:0;top:0;width:1200px;height:47px;background:var(--green);color:var(--white);font-size:16px}
.topbar .item{position:absolute;top:13px;display:flex;align-items:center;gap:10px}
.lang-box{position:absolute;left:1075px;top:15px;width:26px;height:17px;background:#c8d6e8;border:1px solid #fff}
.lang-caret{position:absolute;left:1106px;top:21px;border:5px solid transparent;border-top-color:#fff}
.header{left:0;top:47px;width:1200px;height:84px;background:var(--white)}
.brand{position:absolute;display:flex;align-items:center;gap:12px}
.brand .dot{width:34px;height:34px;border-radius:50%;background:var(--orange)}
.brand .name{font-family:'Raleway',sans-serif;font-weight:600;color:var(--green);font-size:27px;line-height:1;white-space:nowrap}
.brand .tag{font-size:9.5px;color:var(--green);letter-spacing:.3px;text-transform:uppercase;margin-top:5px}
.nav{position:absolute;left:462px;top:23px;display:flex;gap:0;font-size:14px;color:var(--ink)}
.nav a{display:block;padding:0 21px;height:38px;line-height:38px;color:var(--ink);text-decoration:none}
.nav a.active{border:1.5px solid var(--orange);color:var(--orange);padding:0 18px}
.hero{left:0;top:131px;width:1200px;height:534px;background:linear-gradient(120deg,#d9dde3 0%,#9aa3ae 45%,#5d6672 75%,#3e4650 100%)}
.hero-shade{left:0;top:131px;width:1200px;height:534px;background:rgba(20,25,35,.25)}
.hero-text{left:100px;top:348px;width:1000px;text-align:center;color:var(--white);font-family:'Raleway',sans-serif;font-size:31px;line-height:37px;font-weight:400}
.btn-start{left:492px;top:429px;width:214px;height:53px;background:var(--green);border:2px solid #6d8f2a;color:var(--white);font-size:23px;font-weight:700;display:flex;align-items:center;justify-content:center}
.hero-arrow{top:365px}
.services{left:0;top:610px;width:1200px}
.service{position:absolute;width:200px;text-align:center}
.service .ring{width:152px;height:152px;margin:0 auto;border-radius:50%;border:4px solid var(--white);box-shadow:0 0 0 1px #ccc;display:flex;align-items:center;justify-content:center}
.service .ring.green{background:var(--green)}
.service .ring.orange{background:var(--orange)}
.service .label{margin-top:14px;font-size:17px;font-weight:700;color:var(--ink)}
.section-title{position:absolute;left:0;width:1200px;text-align:center;font-family:'Raleway',sans-serif;color:var(--ink)}
.divider{position:absolute;left:340px;width:520px;height:12px}
.divider::before{content:"";position:absolute;left:0;right:0;top:5px;height:2px;background:var(--line)}
.divider::after{content:"";position:absolute;left:254px;top:0;width:12px;height:12px;border-radius:50%;background:#999}
.divider.on-dark::before{background:#777}
.divider.on-dark::after{background:#bbb}
.about-text{left:92px;top:934px;width:1016px;text-align:center;font-size:14.5px;line-height:28.5px;color:var(--body)}
.btn-green{left:531px;top:1085px;width:136px;height:43px;background:var(--green);border:1px solid #1a3205;color:var(--white);font-size:15px;display:flex;align-items:center;justify-content:center}
.quote-bg{left:0;top:1192px;width:1200px;height:519px;background:linear-gradient(135deg,#2a2a2a,#161616 60%,#2b2b2b)}
.steps{left:80px;top:1321px;width:1038px;height:47px}
.step{position:absolute;top:0;height:47px;display:flex;align-items:center;justify-content:center;font-size:14px;color:#333}
.step b{font-size:17px;margin-left:8px;font-weight:700}
.field-label{position:absolute;font-size:15px;font-weight:700;color:var(--white)}
.select{position:absolute;height:53px;border:1px solid #aaa;background:rgba(20,20,20,.55);color:#bbb;font-size:14px;padding:0 18px;display:flex;align-items:center}
.select::after{content:"";position:absolute;right:22px;top:21px;border:8px solid transparent;border-top:10px solid var(--white)}
.btn-next{left:979px;top:1610px;width:141px;height:45px;background:var(--orange);color:var(--white);font-size:15px;font-weight:700;display:flex;align-items:center;justify-content:center}
.avatar{left:84px;top:1809px;width:128px;height:128px;border-radius:50%;border:4px solid var(--green);background:linear-gradient(160deg,#cfd4d8,#8e979f)}
.avatar-tail{left:142px;top:1930px;border:10px solid transparent;border-top:12px solid var(--green)}
.quote-mark{left:246px;top:1790px;font-family:Georgia,serif;font-size:70px;color:#ddd;line-height:1}
.testimonial-text{left:254px;top:1816px;width:846px;font-size:13.8px;line-height:23.5px;color:var(--body)}
.testimonial-rule{left:254px;top:1930px;width:846px;height:1px;background:#e2e2e2}
.testimonial-name{left:252px;top:1937px;color:var(--orange);font-weight:700;font-size:17px}
.dots{left:1062px;top:1941px;display:flex;gap:6px}
.dots span{width:10px;height:10px;border-radius:50%;background:#bbb}
.dots span.on{background:var(--green)}
.news-bg{left:0;top:1998px;width:1200px;height:316px;background:linear-gradient(100deg,#101d33,#1f3355 55%,#0e1a2e)}
.input{position:absolute;height:39px;background:var(--white);font-size:13px;color:#777;padding:0 12px;display:flex;align-items:center}
.btn-orange{left:511px;top:2216px;width:178px;height:43px;background:var(--orange);color:var(--white);font-size:15px;font-weight:700;display:flex;align-items:center;justify-content:center}
.client{position:absolute;top:2441px;width:148px;height:70px;border:1px solid #ccc;background:var(--white);display:flex;align-items:center;justify-content:center;gap:8px;font-size:20px;font-weight:700;color:#222}
.client .mk{width:16px;height:16px;border-radius:50%;background:#222}
.footer{left:0;top:2624px;width:1200px;height:260px;background:var(--footer)}
.footer h4{position:absolute;font-weight:400;font-size:15px;color:var(--white)}
.quick-links{position:absolute;left:80px;top:2709px;list-style:none;font-size:12.5px;color:#ddd;line-height:22.6px}
.quick-links li::before{content:"›";margin-right:8px;color:#aaa}
.contact{position:absolute;left:287px;font-size:12.5px;color:#ddd;line-height:19px;display:flex;gap:12px}
.map{left:564px;top:2683px;width:216px;height:152px;background:linear-gradient(135deg,#cfe0c4,#e6ead8 50%,#b9d3e6)}
.copybar{left:0;top:2884px;width:1200px;height:43px;background:var(--green);color:var(--white);font-size:12.5px}
.social{position:absolute;top:7px;width:30px;height:30px;border-radius:50%;border:1.5px solid var(--white)}
</style>
</head>
<body>

<!-- Top bar -->
<div class="abs topbar">
  <div class="item" style="left:660px">
    <svg width="24" height="17" viewBox="0 0 24 17"><rect width="24" height="17" rx="2" fill="#f7941d"/><path d="M1 1l11 9 11-9" stroke="#fff" stroke-width="1.6" fill="none"/></svg>
    <span>info@kavakverbatica.com</span>
  </div>
  <div class="item" style="left:912px">
    <svg width="22" height="22" viewBox="0 0 22 22"><circle cx="11" cy="6" r="5" fill="#f7941d"/><path d="M1 22c0-7 4-10 10-10s10 3 10 10z" fill="#f7941d"/></svg>
    <span>012.555.0147</span>
  </div>
  <div class="lang-box" role="img" aria-label="Language selector flag"></div>
  <div class="lang-caret"></div>
</div>

<!-- Header -->
<header class="abs header">
  <div class="brand" style="left:78px;top:18px">
    <div class="dot"></div>
    <div>
      <div class="name">Kavak Verbatica</div>
      <div class="tag">Translation, Localization &amp; Consultancy</div>
    </div>
  </div>
  <nav class="nav">
    <a class="active">Home</a><a>Our Services</a><a>Online Translation</a><a>Graphic Designs</a><a>References</a><a>Contact Us</a>
  </nav>
</header>

<!-- Hero -->
<div class="abs hero" role="img" aria-label="Photo of eyeglasses and pens resting on printed documents"></div>
<div class="abs hero-shade"></div>
<div class="abs hero-text">We are a translation and localization firm with file uploading capacity directed to email for quotation</div>
<div class="abs btn-start">Getting Started</div>
<svg class="abs hero-arrow" style="left:30px" width="34" height="70" viewBox="0 0 34 70"><path d="M32 2L2 35l30 33" stroke="#fff" stroke-width="2" fill="none" opacity=".8"/></svg>
<svg class="abs hero-arrow" style="left:1136px" width="34" height="70" viewBox="0 0 34 70"><path d="M2 2l30 33L2 68" stroke="#fff" stroke-width="2" fill="none" opacity=".8"/></svg>

<!-- Services -->
<div class="abs services">
  <div class="service" style="left:66px">
    <div class="ring green"><svg width="70" height="70" viewBox="0 0 70 70"><rect x="6" y="6" width="32" height="32" rx="3" fill="#fff"/><rect x="30" y="30" width="32" height="32" rx="3" fill="#fff" stroke="#335f0c" stroke-width="2"/><path d="M14 16h16M22 12v4M16 30c6-4 10-9 11-14" stroke="#335f0c" stroke-width="2.5" fill="none"/><path d="M38 56l8-20 8 20M41 49h10" stroke="#335f0c" stroke-width="3" fill="none"/></svg></div>
    <div class="label">Translation</div>
  </div>
  <div class="service" style="left:282px">
    <div class="ring orange"><svg width="70" height="70" viewBox="0 0 70 70"><circle cx="20" cy="24" r="7" fill="#fff"/><circle cx="50" cy="24" r="7" fill="#fff"/><path d="M8 48c0-9 5-14 12-14s12 5 12 14zM38 48c0-9 5-14 12-14s12 5 12 14z" fill="#fff"/><rect x="6" y="50" width="58" height="5" fill="#fff"/><path d="M30 12h10" stroke="#fff" stroke-width="3"/></svg></div>
    <div class="label">Interpretation</div>
  </div>
  <div class="service" style="left:499px">
    <div class="ring green"><svg width="70" height="70" viewBox="0 0 70 70"><path d="M35 6c-12 0-20 9-20 20 0 15 20 36 20 36s20-21 20-36C55 15 47 6 35 6z" fill="#fff"/><circle cx="35" cy="26" r="8" fill="#335f0c"/></svg></div>
    <div class="label">Localization</div>
  </div>
  <div class="service" style="left:716px">
    <div class="ring green"><svg width="70" height="70" viewBox="0 0 70 70"><rect x="18" y="8" width="34" height="22" fill="#fff"/><circle cx="14" cy="38" r="6" fill="#fff"/><circle cx="56" cy="38" r="6" fill="#fff"/><circle cx="35" cy="40" r="6" fill="#fff"/><rect x="6" y="50" width="58" height="6" fill="#fff"/><path d="M10 62v-6M60 62v-6" stroke="#fff" stroke-width="3"/></svg></div>
    <div class="label">Consultancy</div>
  </div>
  <div class="service" style="left:932px">
    <div class="ring green"><svg width="70" height="70" viewBox="0 0 70 70"><rect x="8" y="26" width="36" height="26" fill="none" stroke="#fff" stroke-width="3"/><rect x="34" y="10" width="28" height="20" fill="#335f0c" stroke="#fff" stroke-width="3"/><path d="M14 36h24M14 42h16M20 58h12M26 52v6" stroke="#fff" stroke-width="2.5"/></svg></div>
    <div class="label">Translation API</div>
  </div>
</div>

<!-- About -->
<h2 class="section-title" style="top:854px;font-size:27px;font-weight:700;font-family:'Lato',sans-serif">ABOUT KAVAK VERBATICA</h2>
<div class="divider" style="top:903px"></div>
<p class="abs about-text">KVK Translation Services meets the requirements of various organizations working in legal, finance, marketing and advertisement, technical and medical sectors with its expert, qualified translators. Translated documents are delivered in the required format. Our motto is "Delivery on Time with Perfect Quality". Our translation staff consists of language specialists who are all experts in their fields. By implementing the most appropriate visual ideas, we develop designing and printing stages of all kinds of corporate identity, advertisement, publicity and marketing documents which will raise awareness and serve the branding process.</p>
<div class="abs btn-green">Read More</div>

<!-- Quotation form -->
<div class="abs quote-bg" role="img" aria-label="Dark photo of a pen on a laptop keyboard"></div>
<h2 class="section-title" style="top:1228px;font-size:33px;font-weight:400;color:#fff">Translation Quotation Form - 3 Quick Steps</h2>
<div class="divider on-dark" style="top:1285px"></div>
<div class="abs steps">
  <svg class="abs" style="left:0;top:0" width="1038" height="47" viewBox="0 0 1038 47">
    <path d="M0 0h345l11 23.5L345 47H0z" fill="#f7941d"/>
    <path d="M345 0h345l11 23.5L690 47H345l11-23.5z" fill="#cfcfcf"/>
    <path d="M690 0h338l10 23.5L1028 47H690l11-23.5z" fill="#fff"/>
  </svg>
  <div class="step" style="left:0;width:345px">STEP 1: <b>Time &amp; Languages</b></div>
  <div class="step" style="left:355px;width:335px">STEP 2: <b>Upload File</b></div>
  <div class="step" style="left:700px;width:330px">STEP 3: <b>Personal Details</b></div>
</div>
<div class="field-label" style="left:80px;top:1396px">Time Frame</div>
<div class="select" style="left:80px;top:1424px;width:497px">Within 48 Hours</div>
<div class="field-label" style="left:622px;top:1396px">Certification</div>
<div class="select" style="left:622px;top:1424px;width:496px">Select</div>
<div class="field-label" style="left:80px;top:1501px">Translate From</div>
<div class="select" style="left:80px;top:1530px;width:497px">English</div>
<svg class="abs" style="left:584px;top:1543px" width="30" height="26" viewBox="0 0 30 26"><path d="M2 8h24M20 2l6 6-6 6M28 18H4M10 12l-6 6 6 6" stroke="#fff" stroke-width="2" fill="none"/></svg>
<div class="field-label" style="left:622px;top:1501px">Translate To</div>
<div class="select" style="left:622px;top:1530px;width:496px">French</div>
<div class="abs btn-next">Next &nbsp;»</div>

<!-- Testimonials -->
<h2 class="section-title" style="top:1741px;font-size:33px;font-weight:400">Client Testimonials</h2>
<div class="divider" style="top:1785px"></div>
<div class="abs avatar" role="img" aria-label="Portrait photo of the client"></div>
<div class="abs avatar-tail"></div>
<div class="abs quote-mark">“</div>
<p class="abs testimonial-text">&nbsp;&nbsp;&nbsp;&nbsp;&nbsp;&nbsp;&nbsp;Lorem ipsum dolor smit amet, consectetuer adipiscing elitmk, sed amet diam nonummy nibh euismod tincidunt nt ut laoreetml dolore magna aliquam erat volutpat. Ut wisi enim ad minim veniam, quis nostrud exer tationk ullamcorper suscipit lobortisk nisl utml aliqpi ex ea commodo consequat. Duis autem vel eumk iriure dolor inj hendrerit inn vulputate velit esse molestiemo consequat, velhki illumn gnol dolore eu feugiat nulla facilisis .</p>
<div class="abs testimonial-rule"></div>
<div class="abs testimonial-name">- Mr. Arlen Voskuil</div>
<div class="abs dots"><span class="on"></span><span></span><span></span></div>

<!-- Newsletter -->
<div class="abs news-bg" role="img" aria-label="Photo of a businessman in a suit with arms crossed"></div>
<h2 class="section-title" style="top:2040px;font-size:33px;font-weight:400;color:#fff">Newsletter Subscription</h2>
<div class="divider on-dark" style="top:2088px"></div>
<div class="abs" style="left:0;top:2113px;width:1200px;text-align:center;color:#fff;font-size:15px">Lorem ipsum dolor smit amet, consectetuer adipiscing elitmk</div>
<div class="input" style="left:170px;top:2158px;width:415px">Enter your name</div>
<div class="input" style="left:615px;top:2158px;width:415px">Enter your email</div>
<div class="abs btn-orange">SUBSCRIBE NOW</div>

<!-- Clients -->
<h2 class="section-title" style="top:2360px;font-size:33px;font-weight:400">Our Clients</h2>
<div class="divider" style="top:2404px"></div>
<svg class="abs" style="left:36px;top:2455px" width="20" height="42" viewBox="0 0 20 42"><path d="M18 2L2 21l16 19" stroke="#bbb" stroke-width="2" fill="none"/></svg>
<div class="client" style="left:82px"><span class="mk"></span>Norvane</div>
<div class="client" style="left:259px"><span class="mk"></span>Halberk</div>
<div class="client" style="left:437px">Quintaro</div>
<div class="client" style="left:615px;font-size:18px">Lumeo Systems</div>
<div class="client" style="left:792px"><span class="mk"></span>Norvane</div>
<div class="client" style="left:970px">Brightvale</div>
<svg class="abs" style="left:1144px;top:2455px" width="20" height="42" viewBox="0 0 20 42"><path d="M2 2l16 19L2 40" stroke="#bbb" stroke-width="2" fill="none"/></svg>

<!-- Footer -->
<svg class="abs" style="left:0;top:2510px" width="1200" height="116" viewBox="0 0 1200 116" preserveAspectRatio="none">
  <path d="M0 58C300 120 750 120 1200 10V116H0z" fill="#161616"/>
  <path d="M380 112C760 118 1000 60 1200 0V34C1000 92 760 118 380 112z" fill="#f7941d"/>
</svg>
<footer class="abs footer">
  <h4 style="left:80px;top:52px">Quick Links</h4>
  <ul class="quick-links" style="top:85px">
    <li>Home</li><li>Our Services</li><li>Online Translation</li><li>Graphic Designs</li><li>References</li><li>Contact Us</li>
  </ul>
  <h4 style="left:287px;top:52px">Contact Details</h4>
  <div class="contact" style="top:85px">
    <svg width="12" height="16" viewBox="0 0 12 16"><path d="M6 0C3 0 0 2.5 0 6c0 4 6 10 6 10s6-6 6-10c0-3.5-3-6-6-6z" fill="#f7941d"/><circle cx="6" cy="6" r="2.2" fill="#161616"/></svg>
    <span>Lorem ipsum dolor sit amet<br>vim quem primis Quot - 12345</span>
  </div>
  <div class="contact" style="top:137px">
    <svg width="12" height="14" viewBox="0 0 12 14"><path d="M2 0h3l1 4-2 1c1 2 2 3 4 4l1-2 3 1v3c0 1-1 2-2 2C5 13 0 8 0 2c0-1 1-2 2-2z" fill="#f7941d"/></svg>
    <span>(123) 555-0190</span>
  </div>
  <div class="contact" style="top:175px">
    <svg width="14" height="11" viewBox="0 0 14 11"><rect width="14" height="11" fill="#f7941d"/><path d="M0 0l7 6 7-6" stroke="#161616" fill="none"/></svg>
    <span>info@kavakverbatica.com</span>
  </div>
  <div class="brand" style="left:858px;top:90px">
    <div class="dot" style="background:#5a5a5a"></div>
    <div>
      <div class="name" style="color:#9a9a9a;font-weight:400;font-size:30px">Kavak Verbatica</div>
      <div class="tag" style="color:#9a9a9a">Translation, Localization &amp; Consultancy</div>
    </div>
  </div>
</footer>
<div class="abs map" role="img" aria-label="Street map showing the office location"></div>
<svg class="abs" style="left:660px;top:2738px" width="20" height="28" viewBox="0 0 20 28"><path d="M10 0C4 0 0 4 0 10c0 7 10 18 10 18s10-11 10-18C20 4 16 0 10 0z" fill="#d63a2f"/><circle cx="10" cy="10" r="4" fill="#fff"/></svg>
<div class="abs copybar">
  <div class="abs" style="left:80px;top:14px">Copyright © 2016 KAVAK VERBATICA. All Rights Reserved</div>
  <span class="social" style="left:1009px"></span>
  <span class="social" style="left:1048px"></span>
  <span class="social" style="left:1087px"></span>
</div>

</body>
</html>
```